Need Letterhead Design & Matching Business Card

I have a logo that I love already. But the letterhead is less than appealing and boring. I'd like a design for my letterhead which I will match with business cards. Also, I'd like to have used fonts that are generally available, as my current letterhead uses a font named "SPACE" which nobody has unless they download it...so when a Word version is forwarded, it looks awful on the receiver's screed due to not having the font. That being said, modern is the look we like and are going for.

My business is "Hollister Brantley PC" - a law firm specializing in representing people who have suffered catastrophic injuries or death (plane, auto, train crashes etc.).

See attached letterhead, which has all of the pertinent information. My logo is also attached in various formats.

```html
<!DOCTYPE html>
<html lang="en">
<head>
<meta charset="utf-8">
<title>Hollister Brantley PC – Letterhead &amp; Business Card</title>
<link rel="stylesheet" href="https://fonts.googleapis.com/css2?family=Lato:wght@400;700;900&family=Montserrat:wght@400;500;600&family=Questrial&display=swap">
<style>
  :root {
    --backdrop: #cdcdcd;
    --paper: #ffffff;
    --ink: #111111;
    --card-dark: #1b1a18;
    --text-grey: #8e8e8e;
    --body-grey: #a3a3a3;
    --contact-grey: #555555;
    --signature-tone: #ececec;
  }
  * { box-sizing: border-box; margin: 0; padding: 0; }
  html, body { width: 1155px; height: 1200px; overflow: hidden; }
  body { background: var(--backdrop); position: relative; font-family: "Lato", sans-serif; }

  .icon-defs { position: absolute; width: 0; height: 0; }

  /* ---------- Letterhead ---------- */
  .letterhead {
    position: absolute; left: 114px; top: 101px; width: 705px; height: 998px;
    background: var(--paper); overflow: hidden;
  }
  .brand { position: absolute; display: flex; align-items: center; }
  .brand-square { background: var(--ink); flex: none; }
  .brand-name {
    font-family: "Lato", sans-serif; font-weight: 400; color: var(--ink);
    text-transform: uppercase; line-height: 1.05; letter-spacing: 0.01em;
  }
  .letterhead .brand { left: 45px; top: 67px; }
  .letterhead .brand-square { width: 58px; height: 58px; margin-right: 10px; }
  .letterhead .brand-name { font-size: 21px; }

  .contact-list { position: absolute; list-style: none; color: var(--contact-grey); }
  .contact-list li { display: flex; align-items: flex-start; }
  .contact-icon { flex: none; fill: var(--ink); }
  .letterhead .contact-list { left: 520px; top: 49px; font-size: 9.6px; line-height: 12px; }
  .letterhead .contact-list li { margin-bottom: 8px; }
  .letterhead .contact-icon { width: 12px; height: 12px; margin-right: 5px; margin-top: 0; }

  .recipient { position: absolute; left: 45px; top: 268px; font-family: "Montserrat", sans-serif; }
  .recipient-name { font-size: 21px; font-weight: 600; color: var(--ink); margin-bottom: 6px; }
  .recipient-line { font-size: 12.5px; color: var(--text-grey); line-height: 16px; margin-bottom: 7px; }
  .recipient-line.address { line-height: 17px; }

  .letter-body {
    position: absolute; left: 46px; top: 412px; width: 612px;
    font-family: "Questrial", sans-serif; font-size: 15.6px; line-height: 22px;
    color: var(--body-grey); text-align: justify; text-align-last: left;
  }
  .letter-body p { margin-bottom: 22px; }

  .sign-off {
    position: absolute; left: 46px; top: 791px;
    font-family: "Montserrat", sans-serif; font-weight: 500; font-size: 15.5px; color: var(--ink);
  }
  .signature {
    position: absolute; left: 76px; top: 824px; width: 104px; height: 64px;
    background: var(--signature-tone); border-radius: 4px;
  }

  .footer-band { position: absolute; left: 0; background: var(--ink); }
  .letterhead .footer-band {
    bottom: 0; width: 495px; height: 19px;
    clip-path: polygon(0 0, 100% 0, 95.5% 100%, 0 100%);
  }

  /* ---------- Business card – back ---------- */
  .card { position: absolute; overflow: hidden; }
  .card-back {
    left: 643px; top: 284px; width: 344px; height: 212px; background: var(--card-dark);
    display: flex; align-items: center; justify-content: center;
  }
  .card-back .brand { position: static; }
  .card-back .brand-square { width: 30px; height: 30px; border: 1.5px solid var(--paper); background: none; margin-right: 10px; }
  .card-back .brand-name { color: var(--paper); font-size: 14px; }

  /* ---------- Business card – front ---------- */
  .card-front { left: 641px; top: 530px; width: 350px; height: 213px; background: var(--paper); }
  .card-front .brand { left: 24px; top: 25px; }
  .card-front .brand-square { width: 40px; height: 41px; margin-right: 8px; }
  .card-front .brand-name { font-size: 14px; }

  .card-holder { position: absolute; right: 25px; top: 30px; text-align: right; }
  .holder-name { font-family: "Lato", sans-serif; font-size: 12px; font-weight: 900; color: var(--ink); letter-spacing: 0.02em; }
  .holder-role { font-size: 9.5px; color: var(--contact-grey); margin-top: 2px; }
  .holder-rule { width: 32px; height: 1.5px; background: var(--ink); margin: 6px 0 0 auto; }

  .card-front .contact-list { left: 24px; top: 109px; font-size: 7.5px; line-height: 10px; }
  .card-front .contact-list li { margin-bottom: 6px; }
  .card-front .contact-icon { width: 10px; height: 10px; margin-right: 3px; }

  .card-front .footer-band {
    bottom: 0; width: 221px; height: 11px;
    clip-path: polygon(0 0, 100% 0, 94% 100%, 0 100%);
  }
</style>
</head>
<body>

<svg class="icon-defs" aria-hidden="true">
  <defs>
    <symbol id="icon-pin" viewBox="0 0 16 16">
      <rect width="16" height="16"/>
      <path d="M8 2.5a3.6 3.6 0 0 0-3.6 3.6C4.4 9 8 13.5 8 13.5s3.6-4.5 3.6-7.4A3.6 3.6 0 0 0 8 2.5zm0 5.1a1.5 1.5 0 1 1 0-3 1.5 1.5 0 0 1 0 3z" fill="#fff"/>
    </symbol>
    <symbol id="icon-phone" viewBox="0 0 16 16">
      <rect width="16" height="16"/>
      <path d="M5 3h2l1 3-1.4 1a6 6 0 0 0 2.4 2.4L10 8l3 1v2a1.5 1.5 0 0 1-1.6 1.5A8.5 8.5 0 0 1 3.5 4.6 1.5 1.5 0 0 1 5 3z" fill="#fff"/>
    </symbol>
    <symbol id="icon-mail" viewBox="0 0 16 16">
      <rect width="16" height="16"/>
      <rect x="3" y="4.5" width="10" height="7" fill="none" stroke="#fff" stroke-width="1.2"/>
      <path d="M3 4.5l5 4 5-4M3 11.5l3.6-3.3M13 11.5 9.4 8.2" fill="none" stroke="#fff" stroke-width="1.1"/>
    </symbol>
    <symbol id="icon-web" viewBox="0 0 16 16">
      <rect width="16" height="16"/>
      <path d="M5 3v9.5l2.4-2.2 1.6 3.4 1.5-.7-1.6-3.3H12z" fill="#fff"/>
    </symbol>
  </defs>
</svg>

<section class="letterhead">
  <div class="brand">
    <span class="brand-square"></span>
    <span class="brand-name">Hollister<br>Brantley PC</span>
  </div>

  <ul class="contact-list">
    <li><svg class="contact-icon"><use href="#icon-pin"/></svg><span>M. Dorian Vale, Esq. | President<br>4820 Harbor Crest Blvd. | suite 700<br>Lakemont, CA 90410</span></li>
    <li><svg class="contact-icon"><use href="#icon-phone"/></svg><span>(855) 555-0142</span></li>
    <li><svg class="contact-icon"><use href="#icon-mail"/></svg><span>dorian@hollisterbrantley.com</span></li>
    <li><svg class="contact-icon"><use href="#icon-web"/></svg><span>www.hollisterbrantley.com</span></li>
  </ul>

  <div class="recipient">
    <p class="recipient-name">Jone Smith</p>
    <p class="recipient-line">0123-456-789</p>
    <p class="recipient-line">info@youremailaddress.com</p>
    <p class="recipient-line address">1234 City Your Ln. Suite<br>123 Dallas, TX 0000</p>
  </div>

  <div class="letter-body">
    <p>Lorem ipsum dolor sit amet, consectetuer adipiscing elit, sed diam nonummy nibh euismod tincidunt ut laoreet dolore magna aliquam erat volutpat. Ut wisi enim ad minim veniam, quis nostrud exerci tation ullamcorper suscipit lobortis nisl ut aliquip ex ea commodo consequat. Duis autem vel eum iriure dolor in hendrerit in vulputate velit esse molestie consequat, vel illum dolore eu feugiat nulla facilisis at vero eros et accumsan et iusto odio dignissim qui blandit praesent luptatum zzril delenit augue duis dolore te feugait nulla facilisi.</p>
    <p>Lorem ipsum dolor sit amet, cons ectetuer adipiscing elit, sed diam nonummy nibh euismod tincidunt ut laoreet dolore magna aliquam erat volutpat. Ut wisi enim ad minim veniam, quis nostrud exerci tation ullamcorper suscipit lobortis nisl ut aliquip ex ea commodo consequat.</p>
    <p>Lorem ipsum dolor sit amet, consectetuer adipiscing elit, sed diam nonummy nibh euismod tincidunt ut laoreet dolore magna aliquam erat</p>
  </div>

  <p class="sign-off">Mr. Warren T. Ashby</p>
  <div class="signature" role="img" aria-label="Handwritten signature of Warren T. Ashby"></div>

  <div class="footer-band"></div>
</section>

<section class="card card-back">
  <div class="brand">
    <span class="brand-square"></span>
    <span class="brand-name">Hollister<br>Brantley PC</span>
  </div>
</section>

<section class="card card-front">
  <div class="brand">
    <span class="brand-square"></span>
    <span class="brand-name">Hollister<br>Brantley PC</span>
  </div>

  <div class="card-holder">
    <p class="holder-name">WARREN T. ASHBY</p>
    <p class="holder-role">Managing Director</p>
    <div class="holder-rule"></div>
  </div>

  <ul class="contact-list">
    <li><svg class="contact-icon"><use href="#icon-pin"/></svg><span>M. Dorian Vale, Esq. | President<br>4820 Harbor Crest Blvd. | suite 700<br>Lakemont, CA 90410</span></li>
    <li><svg class="contact-icon"><use href="#icon-phone"/></svg><span>(855) 555-0142</span></li>
    <li><svg class="contact-icon"><use href="#icon-mail"/></svg><span>dorian@hollisterbrantley.com</span></li>
    <li><svg class="contact-icon"><use href="#icon-web"/></svg><span>www.hollisterbrantley.com</span></li>
  </ul>

  <div class="footer-band"></div>
</section>

</body>
</html>
```